Website Design for new business Junior Stride Athletics

We need a website for our new business Junior Stride Athletics which is about teaching kids from 5 years to 16 years of age how to play either Australian Rules Football or Soccer. Need area for Soccer and Football plus Coaches section, and schedule for each training etc. NEW LOGO ADDED

Target Market(s)

Adults with kids from 5 to 16 looking for specialist coaches to train their kids

Industry/Entity Type

Fitness

Number of Pages Required

5+ page

Colors
3176b5
ffc214

Requirements
Must have
• Logo
• How, Why and What
Nice to have
• I like this website http://www.bramblewickgames.com.au/
• http://www.quillhavenplaydrills.com.au/ is another site that is okay
Should not have
• Our competitor is this website http://www.marrowvaleyouthclinic.com.au/ but I don't like their website style not kid or parent friendly

```html
<!DOCTYPE html>
<html lang="en">
<head>
<meta charset="utf-8">
<title>Junior Stride Athletics – Where Kids are Champions</title>
<link href="https://fonts.googleapis.com/css2?family=Open+Sans:ital,wght@0,400;0,600;0,700;0,800;1,400&display=swap" rel="stylesheet">
<style>
:root{
  --navy:#0d4a8f;
  --brand-blue:#3176b5;
  --sky:#1a9ae0;
  --yellow:#ffc214;
  --ink:#2b2b2b;
  --white:#ffffff;
  --footer:#2a2a2a;
  --muted:#8a8a8a;
  --grass-light:#8cc64a;
  --grass-dark:#4f8a22;
}
*{margin:0;padding:0;box-sizing:border-box}
html,body{width:1200px;height:2184px;overflow:hidden}
html{background:var(--white)}
body{font-family:'Open Sans',Arial,sans-serif;color:var(--ink);position:relative}
.abs{position:absolute}
a{text-decoration:none}

/* backgrounds */
.hero{left:0;top:140px;width:1200px;height:382px;background:linear-gradient(180deg,var(--grass-light) 0%,var(--grass-dark) 50%,#6fae36 100%)}
.bands{left:0;top:0}

/* header */
.site-header{left:0;top:0;width:1200px;height:150px;background:var(--navy);clip-path:polygon(0 0,100% 0,100% 100%,0 96%)}
.brand{left:96px;top:48px;display:flex;align-items:center;gap:10px}
.brand-dot{width:26px;height:26px;border-radius:50%;background:var(--white)}
.brand-name{color:var(--white);font-weight:700;font-size:18px;line-height:1.15;width:120px}
.tagline{left:273px;top:56px;color:var(--white);font-style:italic;font-size:27px;letter-spacing:.5px}
.trial-btn{left:792px;top:42px;width:324px;height:76px;border-radius:15px;background:var(--yellow);color:#111;font-weight:700;font-size:21px;display:flex;align-items:center;justify-content:center}

/* hero */
.hero-copy{left:0;top:222px;width:1200px;text-align:center;color:var(--white);text-shadow:0 2px 4px rgba(0,0,0,.45)}
.hero-title{font-weight:800;font-size:52px;letter-spacing:1.5px;line-height:64px}
.hero-sub{font-weight:700;font-size:33px;letter-spacing:1px;line-height:42px}
.hero-question{font-weight:600;font-size:24px;margin-top:14px;line-height:34px}
.details-btn{left:467px;top:403px;width:281px;height:63px;border-radius:18px;background:rgba(13,74,143,.88);color:var(--white);font-weight:700;font-size:16px;display:flex;align-items:center;justify-content:center}

/* sections */
.section-title{font-weight:800;font-size:36px;letter-spacing:1.5px;line-height:44px}
.section-text{font-size:19px;line-height:36px;letter-spacing:.3px}
.read-more{font-size:16px;display:flex;align-items:center;gap:6px}
.photo{background:linear-gradient(160deg,#e9e2d6,#c9b8a0)}

.why-title{left:93px;top:572px;color:var(--navy)}
.why-text{left:96px;top:624px;width:620px;line-height:30px}
.why-more{left:96px;top:700px;color:var(--navy)}

.how-title{left:387px;top:904px;color:var(--white);text-shadow:0 2px 3px rgba(0,0,0,.35)}
.how-text{left:387px;top:959px;width:740px}
.how-more{left:387px;top:1124px;color:var(--ink)}

.what-title{left:228px;top:1306px;color:var(--sky)}
.what-text{left:234px;top:1353px;width:545px}
.what-more{left:234px;top:1508px;color:var(--sky)}

/* coaches */
.coaches-title{left:0;top:1690px;width:1200px;text-align:center;color:var(--yellow)}
.coaches-sub{left:0;top:1732px;width:1200px;text-align:center;color:#e6eef8;font-size:22px;letter-spacing:3px}
.coach-photo{left:122px;top:1787px;width:190px;height:190px;border-radius:50%;border:7px solid #dfe8f3;background:linear-gradient(160deg,#7a8a99,#2c3440)}
.coach-bio{left:340px;top:1815px;width:760px;color:#e8eef6}
.coach-name{font-size:22px;font-weight:400;color:var(--white);line-height:32px}
.coach-name strong{font-weight:700}
.coach-text{font-size:17px;line-height:27px;letter-spacing:.3px}

/* footer */
.site-footer{left:0;top:2036px;width:1200px;height:148px;background:var(--footer);border-top:2px solid #9db6d3}
.contact-label{left:87px;top:2074px;color:var(--white);font-weight:700;font-size:18px}
.contact-email{left:84px;top:2108px;color:var(--sky);font-weight:600;font-size:19px}
.copyright{left:0;top:2104px;width:1200px;text-align:center;color:var(--muted);font-size:14px;font-weight:600}
.social-label{left:936px;top:2064px;width:160px;text-align:center;color:var(--white);font-size:16px;font-weight:600}
.social-list{left:917px;top:2112px;display:flex;gap:16px;list-style:none}
.social-list li{width:36px;height:36px;border-radius:50%;background:#111}
</style>
</head>
<body>

<div class="abs hero" role="img" aria-label="Close-up photo of a green grass sports field"></div>

<svg class="abs bands" width="1200" height="2040" viewBox="0 0 1200 2040" aria-hidden="true">
  <polygon points="368,852 1200,768 1200,1282 278,1190" fill="#ffc214"/>
  <polygon points="0,1752 1200,1530 1200,2040 0,2040" fill="#3176b5"/>
</svg>

<header class="abs site-header"></header>
<div class="abs brand"><span class="brand-dot"></span><span class="brand-name">Junior Stride Athletics</span></div>
<p class="abs tagline">Where Kids are Champions</p>
<a class="abs trial-btn">TWO WEEK FREE TRIAL</a>

<section class="abs hero-copy">
  <h1 class="hero-title">SPECIALIST SPORTS COACHING</h1>
  <p class="hero-sub">FOR BOYS &amp; GIRLS 5 TO 16 YEARS OLD</p>
  <p class="hero-question">Is your child the next champion?</p>
</section>
<a class="abs details-btn">Click here for details</a>

<!-- why -->
<div class="abs photo" style="left:780px;top:585px;width:280px;height:340px;border-radius:40px" role="img" aria-label="Photo of a boy in a striped football kit sitting and pointing, holding a soccer ball"></div>
<h2 class="abs section-title why-title">WHY WE DO IT</h2>
<p class="abs section-text why-text">We are all about getting kids away from computer games and to start living life in a healthy and productive way.</p>
<a class="abs read-more why-more">Read More <svg width="24" height="6" viewBox="0 0 24 6"><path d="M0 3h22M18 0.5l4 2.5-4 2.5" stroke="currentColor" fill="none"/></svg></a>

<!-- how -->
<div class="abs photo" style="left:0;top:780px;width:290px;height:415px;border-radius:0 60px 60px 0" role="img" aria-label="Photo of a boy in a white shirt juggling a soccer ball"></div>
<h2 class="abs section-title how-title">HOW WE DO IT</h2>
<p class="abs section-text how-text">We start teaching boys &amp; girls from 5 years old basic skills of how to play their chosen sport. We introduce aspects of nutrition, fitness, physical preparation, injury prevention and other advanced concepts as your child progresses up until 16 years of age.</p>
<a class="abs read-more how-more">Read More <svg width="24" height="6" viewBox="0 0 24 6"><path d="M0 3h22M18 0.5l4 2.5-4 2.5" stroke="currentColor" fill="none"/></svg></a>

<!-- what -->
<div class="abs" style="left:915px;top:1180px;width:173px;height:173px;border-radius:50%;background:radial-gradient(circle at 40% 35%,#ffffff,#c8c8c8)" role="img" aria-label="Photo of a soccer ball"></div>
<div class="abs photo" style="left:800px;top:1320px;width:395px;height:210px;border-radius:60px;background:linear-gradient(160deg,#cfe3f5,#6a9fd0)" role="img" aria-label="Photo of a young goalkeeper diving sideways"></div>
<div class="abs photo" style="left:0;top:1225px;width:170px;height:515px;border-radius:0 50px 50px 0;background:linear-gradient(180deg,#d8d8d8,#5bbf7a)" role="img" aria-label="Photo of a boy in green trousers kicking a ball"></div>
<h2 class="abs section-title what-title">WHAT WE DO</h2>
<p class="abs section-text what-text">We hold weekly sessions for kids from 5 to 8, 9 to 12 and 12 to 16 years of age. We also have 3 day holiday programs and for those children that have talent and want to explore their chosen sport further we have elite squads.</p>
<a class="abs read-more what-more">Read More <svg width="24" height="6" viewBox="0 0 24 6"><path d="M0 3h22M18 0.5l4 2.5-4 2.5" stroke="currentColor" fill="none"/></svg></a>

<!-- coaches -->
<h2 class="abs section-title coaches-title">COACHES</h2>
<p class="abs coaches-sub">Australian Rules</p>
<div class="abs coach-photo" role="img" aria-label="Portrait photo of coach Daniel Marsh"></div>
<div class="abs coach-bio">
  <h3 class="coach-name">About <strong>Daniel Marsh</strong></h3>
  <p class="coach-text">Daniel Marsh played over 200 games of football for Old Brackenridge, Fernleigh &amp; Coralbay over his decade of playing the game. He is one who loves the game and wants to teach others how to play and have fun.</p>
</div>

<!-- footer -->
<footer class="abs site-footer"></footer>
<p class="abs contact-label">Have a question or comment</p>
<a class="abs contact-email">daniel@juniorstride.com.au</a>
<p class="abs copyright">© 2016 Junior Stride Athletics Pty Ltd</p>
<p class="abs social-label">Get Social</p>
<ul class="abs social-list" aria-label="Social links">
  <li></li><li></li><li></li><li></li>
</ul>

</body>
</html>
```